Business card

I need to make clear the my status by my works acceptance in academia and pop culture.

The format of the card in the pics uploaded is an approximation. Something new may work or you make just tweak this design to make it more powerful.

```html
<!DOCTYPE html>
<html lang="en">
<head>
<meta charset="utf-8">
<title>Martin Velsbruck, Ph.D — Business Card</title>
<link rel="stylesheet" href="https://fonts.googleapis.com/css2?family=Bebas+Neue&family=Roboto:ital,wght@0,400;0,500;0,700;1,400;1,500;1,700&display=swap">
<style>
  :root {
    --backdrop: #c2c2c2;
    --card-light: #e4e3e5;
    --card-dark: #1c1c1c;
    --ink-dark: #1e1e1e;
    --ink-light: #f4f4f4;
    --ink-muted: #bdbdbd;
  }
  * { margin: 0; padding: 0; box-sizing: border-box; }
  html, body { width: 1200px; height: 1101px; overflow: hidden; }
  body {
    background: var(--backdrop);
    font-family: "Roboto", Arial, sans-serif;
    position: relative;
  }
  .card {
    position: absolute;
    width: 302px;
    height: 529px;
  }
  .card--front { left: 246px; top: 269px; background: var(--card-light); color: var(--ink-dark); }
  .card--back  { left: 641px; top: 267px; background: var(--card-dark); color: var(--ink-light); }
  .card > * { position: absolute; }

  .name {
    left: 27px; top: 42px;
    font-family: "Bebas Neue", Impact, sans-serif;
    font-size: 38px; line-height: 38px; font-weight: 400;
    letter-spacing: 0.2px;
  }
  .quote-mark { width: 32px; height: 25px; }
  .quote-mark path { fill: currentColor; }
  .quote-line {
    font-style: italic; font-weight: 700;
    font-size: 15.5px; line-height: 20px;
  }
  .blurb {
    left: 32px; top: 345px;
    font-style: italic; font-size: 13px; line-height: 17.5px;
  }
  .divider {
    left: 32px; width: 239px; height: 14px;
  }
  .divider line { stroke: currentColor; stroke-width: 1; }
  .divider rect { fill: currentColor; }
  .cta-label {
    left: 0; width: 100%; top: 462px; text-align: center;
    font-style: italic; font-size: 13px;
  }
  .web {
    left: 0; width: 100%; top: 483px; text-align: center;
    font-weight: 700; font-size: 17px; letter-spacing: 0.9px;
  }

  .heading {
    left: 30px; top: 39px;
    font-weight: 700; font-size: 15px; line-height: 20px;
  }
  .list {
    left: 31px; list-style: none;
    font-size: 13.5px; line-height: 18px;
  }
  .list li::before { content: "•"; margin-right: 5px; font-size: 11px; }
  .list--museums { top: 99px; }
  .list--films { top: 205px; }
  .films-label {
    left: 30px; top: 172px;
    font-style: italic; font-size: 13.5px; color: var(--ink-muted);
  }
  .card--back .quote-mark { left: 31px; top: 291px; color: var(--ink-muted); }
  .testimonial {
    left: 30px; top: 327px;
    font-style: italic; font-weight: 700; font-size: 17.5px; line-height: 23px;
  }
  .attribution {
    left: 31px; top: 379px;
    font-style: italic; font-weight: 500; font-size: 11px;
  }
  .contact {
    left: 0; width: 100%; top: 454px; text-align: center;
    font-weight: 700; font-size: 17.5px; line-height: 23px;
  }
</style>
</head>
<body>

<section class="card card--front">
  <h1 class="name">Martin<br>Velsbruck, Ph.D</h1>

  <svg class="quote-mark" style="left:28px;top:157px" viewBox="0 0 32 25" aria-hidden="true">
    <path d="M7 25a7 7 0 1 1 6-10.5C13 6 9 2 5 0l1.5-1C13 2 14 10 14 17a7 7 0 0 1-7 8z"/>
    <path d="M25 25a7 7 0 1 1 6-10.5C31 6 27 2 23 0l1.5-1C31 2 32 10 32 17a7 7 0 0 1-7 8z"/>
  </svg>
  <p class="quote-line" style="left:28px;top:197px">The Hartwell and<br>Ostrand of Psychology &amp; History</p>

  <svg class="quote-mark" style="left:28px;top:254px" viewBox="0 0 32 25" aria-hidden="true">
    <path d="M7 25a7 7 0 1 1 6-10.5C13 6 9 2 5 0l1.5-1C13 2 14 10 14 17a7 7 0 0 1-7 8z"/>
    <path d="M25 25a7 7 0 1 1 6-10.5C31 6 27 2 23 0l1.5-1C31 2 32 10 32 17a7 7 0 0 1-7 8z"/>
  </svg>
  <p class="quote-line" style="left:28px;top:292px">The Laurel Prize is a Sure Thing.</p>

  <p class="blurb">A Kingsbridge Museum Exhibition Featured<br>Martin’s Ideas. Martin’s Bio-Sociology Has<br>Restructured the Liberal Arts</p>

  <svg class="divider" style="top:427px" viewBox="0 0 239 14" aria-hidden="true">
    <line x1="0" y1="7" x2="85" y2="7"/>
    <line x1="154" y1="7" x2="239" y2="7"/>
    <rect x="93" y="2" width="10" height="10" transform="rotate(45 98 7)"/>
    <rect x="114.5" y="2" width="10" height="10" transform="rotate(45 119.5 7)"/>
    <rect x="136" y="2" width="10" height="10" transform="rotate(45 141 7)"/>
  </svg>

  <p class="cta-label">For Canonical Status:</p>
  <p class="web">www.martin-velsbruck.org</p>
</section>

<section class="card card--back">
  <h2 class="heading">Martin’s Bio-Psych is Fundamental<br>To All Museums Such As:</h2>
  <ul class="list list--museums">
    <li>The Grand Arcade Gallery</li>
    <li>The Harbor City Museum</li>
    <li>The Old Abbey Collection</li>
  </ul>
  <p class="films-label">and the films:</p>
  <ul class="list list--films">
    <li>Starlight Runner 1986</li>
    <li>Tidewell and The Iron Serpent</li>
    <li>River Quest</li>
  </ul>

  <svg class="quote-mark" viewBox="0 0 32 25" aria-hidden="true">
    <path d="M7 25a7 7 0 1 1 6-10.5C13 6 9 2 5 0l1.5-1C13 2 14 10 14 17a7 7 0 0 1-7 8z"/>
    <path d="M25 25a7 7 0 1 1 6-10.5C31 6 27 2 23 0l1.5-1C31 2 32 10 32 17a7 7 0 0 1-7 8z"/>
  </svg>
  <p class="testimonial">Martin Maybe the<br>Greatest Geniun in History</p>
  <p class="attribution">Cognitive Scientist, Northfield University</p>

  <svg class="divider" style="top:429px" viewBox="0 0 239 14" aria-hidden="true">
    <line x1="0" y1="7" x2="85" y2="7"/>
    <line x1="154" y1="7" x2="239" y2="7"/>
    <rect x="93" y="2" width="10" height="10" transform="rotate(45 98 7)"/>
    <rect x="114.5" y="2" width="10" height="10" transform="rotate(45 119.5 7)"/>
    <rect x="136" y="2" width="10" height="10" transform="rotate(45 141 7)"/>
  </svg>

  <p class="contact">555-014-2290<br>velsbruck@mailpost.net</p>
</section>

</body>
</html>
```